Sparkwell Brochure site for a cleaning company based in the UK

We need a site that can sell our products and services to both attract new customer and new cleaners, It needs to be simple but informative and will link to a separate booking site already written. It preferable needs to be written in wordpress and we would require the homepage and template designed, with rights to all images and fonts.

Sparkwell is a cleaning services site offering the domestic client the ability to select from multiple cleaners and it uses our years of industry knowledge to identify the cleaners needs and match that to the correct cleaner and for the most appropriate time. Therefore the site needs to specifically target our customers whilst attracting new cleaners.

The brochure site needs to sell our services and the unique USP of our matching algorithms. This is particularly important for potential cleaners as we only offer them jobs that match their availability profile and their specific skills.

We have an existing booking site and we have attached 2 screenshots detailing the colour scheme and the feel of the site. This brochure site must match these colours and its look and feel.

The site needs to be designed on a mobile first approach as our targeted audience are mobile heavy users. It must also work across as many modern devices as possible.

Target Market(s)

UK Domestic maid cleaning

Industry/Entity Type

Cleaning Service

Coding

Coded - Design and coding required

Number of Pages Required

2 page

Font styles to use
Sans Serif

Requirements
Must have
• Attached Logo
• Menu system with the following pages (pages not designed but menu working)
• - Company Profile
• - Our Service
• - Contact Us
• - Why Sparkwell - both for customers and cleaners
• - Areas we work
• - Want to be a cleaner
• Wordpress site with the following
• - Homepage fully designed with images and font
• - The page template created
• Fully responsive design across all devices (Mobile first)
• See attached screenshots of the booking site for an idea on the colour scheme that needs to be followed.
• Photos and images
Nice to have
• Map for contact us and Areas we work

```html
<!DOCTYPE html>
<html lang="en">
<head>
<meta charset="utf-8">
<title>Sparkwell – Domestic Cleaning</title>
<link href="https://fonts.googleapis.com/css2?family=Lato:wght@400;700;900&family=Open+Sans:wght@400;600;700&display=swap" rel="stylesheet">
<style>
:root{
  --green:#a3c03a;
  --green-dark:#8aa82a;
  --red:#ec6271;
  --card-green:#8cc152;
  --card-yellow:#f1c65a;
  --card-blue:#4fa3c9;
  --card-pink:#e080e2;
  --ink:#222;
  --text:#555;
  --grey-bg:#efefef;
  --line:#d6d6d6;
  --white:#fff;
}
*{box-sizing:border-box;margin:0;padding:0}
html,body{width:1200px;height:3226px;overflow:hidden;background:var(--white)}
body{font-family:"Open Sans",sans-serif;color:var(--text);position:relative}
.abs{position:absolute}
h2,h3,h4{font-family:"Lato",sans-serif;color:var(--ink)}
.section-title{position:absolute;left:0;width:1200px;text-align:center;font-size:27px;font-weight:900;color:var(--ink);letter-spacing:.5px}
.section-sub{position:absolute;left:0;width:1200px;text-align:center;font-size:12px;color:#444}
.btn-small{position:absolute;background:var(--green);color:#fff;font-size:11px;font-weight:600;text-transform:uppercase;padding:0 14px;height:30px;line-height:30px;border-radius:3px}

/* header */
.site-header{position:absolute;top:0;left:0;width:1200px;height:99px;background:#fff}
.brand{position:absolute;left:97px;top:14px;display:flex;flex-direction:column;align-items:center}
.brand-dot{width:44px;height:44px;border-radius:50%;background:var(--green)}
.brand-name{font-family:"Lato",sans-serif;font-weight:700;font-size:17px;color:var(--green);margin-top:6px;letter-spacing:.5px}
.topbar{position:absolute;right:103px;top:17px;display:flex;gap:28px;font-size:11.5px;color:#444}
.topbar span{display:flex;align-items:center;gap:8px}
.topbar i{display:inline-block;width:9px;height:9px;border-radius:50%;background:var(--green)}
.main-nav{position:absolute;right:103px;top:58px;display:flex;gap:23px;font-size:15px;color:#222}

/* hero */
.hero{position:absolute;top:99px;left:0;width:1200px;height:507px;background:linear-gradient(120deg,#8c8a7f 0%,#b9b5a6 35%,#9c9a86 60%,#6d7a4e 100%)}
.hero::after{content:"";position:absolute;inset:0;background:rgba(0,0,0,.22)}
.hero-content{position:absolute;z-index:2;left:0;top:158px;width:1200px;text-align:center;color:#fff}
.hero-content h1{font-family:"Lato",sans-serif;font-weight:900;font-size:36px;letter-spacing:.5px}
.hero-content p{font-size:13px;width:560px;margin:14px auto 0;line-height:1.6}
.hero-btn{display:inline-block;margin-top:22px;border:2px solid #fff;color:#fff;font-size:11px;font-weight:600;padding:8px 14px}
.hero-dots{position:absolute;z-index:2;top:410px;left:550px;display:flex;gap:12px}
.hero-dots i{width:20px;height:4px;background:#fff;opacity:.8}
.hero-dots i.active{background:var(--red);opacity:1}

/* services */
.service-card{position:absolute;top:753px;width:181px;height:296px;color:#fff;text-align:center;box-shadow:0 2px 4px rgba(0,0,0,.15)}
.service-card h3{color:#fff;font-family:"Lato",sans-serif;font-size:16px;font-weight:700;margin-top:25px;text-transform:uppercase}
.service-icon{width:86px;height:86px;border-radius:50%;background:#fff;margin:16px auto 0;display:flex;align-items:center;justify-content:center}
.service-card p{font-size:12px;line-height:1.75;padding:0 22px;margin-top:34px}
.c-red{background:var(--red)}.c-green{background:var(--card-green)}.c-yellow{background:var(--card-yellow)}.c-blue{background:var(--card-blue)}.c-pink{background:var(--card-pink)}

/* about */
.about{position:absolute;top:1129px;left:0;width:1200px;height:339px;background:var(--grey-bg)}
.about h2{position:absolute;left:103px;top:72px;font-size:27px;font-weight:900}
.about p{position:absolute;left:103px;top:118px;width:590px;font-size:12px;line-height:1.9;color:#444}
.about-photo{position:absolute;left:714px;top:45px;width:383px;height:245px;border:5px solid #fff;background:linear-gradient(135deg,#dfe3e6,#b8c1c7 55%,#7f96a8)}

/* staff */
.staff-heading{position:absolute;left:100px;top:1618px;font-size:21px;font-weight:900}
.staff-text{position:absolute;left:100px;top:1665px;width:510px;font-size:12px;line-height:1.9;color:#444}
.staff-card{position:absolute;top:1610px;width:160px;text-align:center}
.staff-photo{width:160px;height:128px;border:5px solid #fff;box-shadow:0 1px 4px rgba(0,0,0,.25)}
.staff-card h4{font-size:15px;font-weight:700;margin-top:18px}
.staff-card span{display:block;font-size:15px;color:#555;margin-top:3px}

/* testimonials */
.testimonials{position:absolute;top:1858px;left:0;width:1200px;height:382px;background:linear-gradient(90deg,#4a443d,#6b6256 45%,#5a5348)}
.testimonials::after{content:"";position:absolute;inset:0;background:rgba(0,0,0,.28)}
.testi-person{position:absolute;z-index:1;left:910px;top:68px;width:190px;height:314px;border-radius:80px 80px 0 0;background:linear-gradient(180deg,#d9c2a8,#c9533e 40%,#eaeaea 70%)}
.testi-title{position:absolute;z-index:2;left:0;top:44px;width:1200px;text-align:center;color:#fff;font-family:"Lato",sans-serif;font-weight:900;font-size:27px}
.testi-sub{position:absolute;z-index:2;left:0;top:92px;width:1200px;text-align:center;color:#fff;font-size:12px}
.quote{position:absolute;z-index:2;top:137px;width:237px;height:116px;background:#fff;font-size:12px;line-height:1.9;color:#333;text-align:center;padding:22px 20px}
.quote::after{content:"";position:absolute;left:106px;bottom:-12px;border:12px solid transparent;border-bottom:0;border-top-color:#fff}
.quote-name{position:absolute;z-index:2;top:279px;width:237px;text-align:center;color:#fff}
.quote-name b{display:block;font-size:14px;font-family:"Lato",sans-serif}
.quote-name span{display:block;font-size:11px;margin-top:6px}

/* booking */
.booking-form{position:absolute;left:103px;top:2376px;width:503px}
.field{height:37px;border:1px solid #ccc;font-size:11px;color:#666;padding:0 16px;line-height:35px;margin-bottom:19px}
.form-btn{height:38px;line-height:38px;text-align:center;color:#fff;font-weight:600;font-size:14px;margin-bottom:18px}
.form-btn.login{background:var(--green)}
.form-btn.register{background:var(--red)}
.forgot{text-align:center;font-size:15px;color:#333;font-weight:600;margin-top:12px}
.booking-photo{position:absolute;left:731px;top:2279px;width:441px;height:409px;border-radius:180px 180px 0 0;background:linear-gradient(160deg,#f4e4d6,#f1c5a0 35%,#5b8ed6 65%,#e6d634)}

/* stats */
.stats{position:absolute;top:2688px;left:0;width:1200px;height:215px;background:var(--green);color:#fff}
.stat{position:absolute;top:50px;width:200px;text-align:center}
.stat svg{display:block;margin:0 auto}
.stat b{display:block;font-size:23px;font-weight:400;margin-top:10px}
.stat span{display:block;font-size:15px}

/* footer */
.footer-brand{position:absolute;left:0;top:2935px;width:1200px;display:flex;flex-direction:column;align-items:center}
.footer-nav{position:absolute;left:0;top:3058px;width:1200px;display:flex;justify-content:center;gap:22px;font-size:15px;color:#333}
.socials{position:absolute;left:0;top:3106px;width:1200px;display:flex;justify-content:center;gap:18px}
.socials i{width:44px;height:44px;border-radius:50%;border:1px solid var(--red)}
.footer-line{position:absolute;left:103px;top:3178px;width:994px;height:1px;background:var(--line)}
.copyright{position:absolute;left:0;top:3194px;width:1200px;text-align:center;font-size:11px;color:#333}
</style>
</head>
<body>

<header class="site-header">
  <div class="brand"><div class="brand-dot"></div><div class="brand-name">SPARKWELL</div></div>
  <div class="topbar">
    <span><i></i>(+1) 555 010 2040</span>
    <span><i></i>Have any questions?</span>
    <span><i></i>Our Locations</span>
  </div>
  <nav class="main-nav">
    <span>Home</span><span>Profile</span><span>Our Service</span><span>Why Sparkwell</span><span>Areas we work</span><span>Want to be a cleaner ?</span><span>Contact Us</span>
  </nav>
</header>

<section class="hero" role="img" aria-label="Photo of cleaners vacuuming and tidying a bright living room">
  <div class="hero-content">
    <h1>WELCOME TO SPARKWELL</h1>
    <p>offering the domestic client the ability to select from multiple cleaners and it uses our years of industry knowledge to identify the cleaners needs and match that to the correct cleaner</p>
    <span class="hero-btn">EVEN FURTHER</span>
  </div>
  <div class="hero-dots"><i></i><i class="active"></i><i></i></div>
</section>

<section class="services">
  <h2 class="section-title" style="top:665px">OUR SERVICES</h2>
  <p class="section-sub" style="top:709px">Get Satisfied with the services we provide A to Z in Cleaning</p>

  <div class="service-card c-red" style="left:103px"><h3>Cleaning</h3>
    <div class="service-icon"><svg width="44" height="44" viewBox="0 0 44 44" fill="none" stroke="#ec6271" stroke-width="3"><path d="M30 6 20 24"/><path d="M14 22l12 6-6 12-12-8z"/></svg></div>
    <p>The standard chunk of Lorem Ipsum used since the 1500s is reproduced below for those interested.</p></div>
  <div class="service-card c-green" style="left:306px"><h3>Linen</h3>
    <div class="service-icon"><svg width="44" height="44" viewBox="0 0 44 44" fill="none" stroke="#8cc152" stroke-width="3"><rect x="8" y="5" width="28" height="34" rx="2"/><circle cx="22" cy="25" r="8"/><path d="M8 13h28"/></svg></div>
    <p>The standard chunk of Lorem Ipsum used since the 1500s is reproduced below for those interested.</p></div>
  <div class="service-card c-yellow" style="left:509px"><h3>Ironing</h3>
    <div class="service-icon"><svg width="46" height="44" viewBox="0 0 46 44" fill="none" stroke="#f1c65a" stroke-width="3"><path d="M6 32h34V26c0-8-8-12-18-12H14"/><path d="M6 32c0-8 6-12 14-12h20"/></svg></div>
    <p>The standard chunk of Lorem Ipsum used since the 1500s is reproduced below for those interested.</p></div>
  <div class="service-card c-blue" style="left:712px"><h3>Oven</h3>
    <div class="service-icon"><svg width="46" height="44" viewBox="0 0 46 44" fill="none" stroke="#4fa3c9" stroke-width="3"><rect x="5" y="9" width="36" height="26" rx="2"/><rect x="10" y="14" width="20" height="16"/><path d="M35 15v2M35 21v2"/></svg></div>
    <p>The standard chunk of Lorem Ipsum used since the 1500s is reproduced below for those interested.</p></div>
  <div class="service-card c-pink" style="left:915px"><h3>Fridge Freezer</h3>
    <div class="service-icon"><svg width="44" height="44" viewBox="0 0 44 44" fill="none" stroke="#e080e2" stroke-width="3"><rect x="11" y="4" width="22" height="36" rx="2"/><path d="M11 17h22M15 9v4M15 22v6"/></svg></div>
    <p>The standard chunk of Lorem Ipsum used since the 1500s is reproduced below for those interested.</p></div>
</section>

<section class="about">
  <h2>ABOUT US</h2>
  <p>There are many variations of passages of Lorem Ipsum available, but the majority have suffered alteration in some form, by injected humour, or randomised words which don't look even slightly believable. If you are going to use a passage of Lorem Ipsum, you need to be sure there isn't anything embarrassing hidden in the middle of text.</p>
  <span class="btn-small" style="left:103px;top:228px">Read More</span>
  <div class="about-photo" role="img" aria-label="Photo of a cleaning team at work in a bright office"></div>
</section>

<section class="staff">
  <h2 class="section-title" style="top:1523px">OUR STAFF</h2>
  <p class="section-sub" style="top:1566px">We all have to go through a thorough training process to provide high quality service</p>
  <h3 class="staff-heading">WE ARE AMAZING PEOPLE!</h3>
  <p class="staff-text">Contrary to popular belief, Lorem Ipsum is not simply random text. It has roots in a piece of classical Latin literature from 45 BC, making it over 2000 years old.</p>
  <span class="btn-small" style="left:100px;top:1756px">View All Team</span>

  <div class="staff-card" style="left:552px"><div class="staff-photo" role="img" aria-label="Photo of a cleaner holding supplies" style="background:linear-gradient(135deg,#e9ecef,#8fb3d9 60%,#c98cc8)"></div><h4>ARUN DALE</h4><span>Cleaning Staff</span></div>
  <div class="staff-card" style="left:745px"><div class="staff-photo" role="img" aria-label="Photo of a cleaner scrubbing an oven" style="background:linear-gradient(135deg,#dfe6ec,#9fb7c8 55%,#d58fb2)"></div><h4>LENA MOSS</h4><span>Cleaning Staff</span></div>
  <div class="staff-card" style="left:939px"><div class="staff-photo" role="img" aria-label="Photo of a smiling cleaner" style="background:linear-gradient(135deg,#e4e4e0,#b6b3ad 55%,#7e8fa0)"></div><h4>PRIYA HALE</h4><span>Cleaning Staff</span></div>
</section>

<section class="testimonials" role="img" aria-label="Background photo of a person mopping a living room floor">
  <div class="testi-person" role="img" aria-label="Photo of a cleaner in an apron holding a bucket of supplies"></div>
  <h2 class="testi-title">TESTIMONIALS</h2>
  <p class="testi-sub">I must explain to you how all this mistaken idea of denouncing pleasure and praising pain was born</p>
  <div class="quote" style="left:103px">“ Lorem ipsum dolor consectetur adipiscing elit, sed do eiusmod at tempor incididunt ut labore ”</div>
  <div class="quote" style="left:372px">“ Lorem ipsum dolor consectetur adipiscing elit, sed do eiusmod at tempor incididunt ut labore ”</div>
  <div class="quote" style="left:641px">“ Lorem ipsum dolor consectetur adipiscing elit, sed do eiusmod at tempor incididunt ut labore ”</div>
  <div class="quote-name" style="left:103px"><b>LENA MOSS</b><span>Manager</span></div>
  <div class="quote-name" style="left:372px"><b>LENA MOSS</b><span>Manager</span></div>
  <div class="quote-name" style="left:641px"><b>LENA MOSS</b><span>Manager</span></div>
</section>

<section class="booking">
  <h2 class="section-title" style="top:2296px;width:580px;left:60px">SERVICE BOOKING</h2>
  <div class="booking-form">
    <div class="field">Enter your mail</div>
    <div class="field">Password</div>
    <div class="form-btn login">Login</div>
    <div class="form-btn register">Register</div>
    <div class="forgot">Forgotten Password ?</div>
  </div>
  <div class="booking-photo" role="img" aria-label="Photo of a smiling cleaner holding a basket of cleaning products"></div>
</section>

<section class="stats">
  <div class="stat" style="left:68px"><svg width="46" height="46" viewBox="0 0 46 46" fill="none" stroke="#fff" stroke-width="3"><circle cx="23" cy="23" r="20"/><path d="M14 23l6 6 12-12"/></svg><b>2000</b><span>satisfied customer</span></div>
  <div class="stat" style="left:287px"><svg width="46" height="46" viewBox="0 0 46 46" fill="#fff"><path d="M42 4 4 20l13 5 3 14 6-9 10 8z"/></svg><b>5000</b><span>project finished</span></div>
  <div class="stat" style="left:504px"><svg width="46" height="46" viewBox="0 0 46 46" fill="none" stroke="#fff" stroke-width="3"><circle cx="23" cy="23" r="20"/><path d="M23 11v12h9"/></svg><b>10</b><span>years of experience</span></div>
  <div class="stat" style="left:717px"><svg width="46" height="46" viewBox="0 0 46 46" fill="#fff"><rect x="4" y="20" width="8" height="22"/><path d="M15 20 24 4c4 0 5 3 4 7l-2 7h14c3 0 4 3 3 5l-5 17c-1 2-2 2-4 2H15z"/></svg><b>100%</b><span>Quality</span></div>
  <div class="stat" style="left:926px"><svg width="50" height="46" viewBox="0 0 50 46" fill="#fff"><path d="M4 6h28v18H14l-7 6v-6H4z"/><path d="M35 14h11v18h-4v6l-7-6H18v-4h17z"/></svg><b>2000</b><span>cleaning tip advices</span></div>
</section>

<footer>
  <div class="footer-brand"><div class="brand-dot" style="width:52px;height:52px"></div><div class="brand-name" style="font-size:18px">SPARKWELL</div></div>
  <nav class="footer-nav"><span>Home</span><span>Profile</span><span>Our Service</span><span>Why Sparkwell</span><span>Areas we work</span><span>Contact Us</span></nav>
  <div class="socials"><i></i><i></i><i></i><i></i><i></i></div>
  <div class="footer-line"></div>
  <p class="copyright">© Copyright 2017 Brightside Studio. All Rights Reserved</p>
</footer>

</body>
</html>
```